Building company business card

Design and print business cards for BRENTHOLM PTY LTD.
A residantial homes building company.
Mark Lantern already designed the company Logo.

```html
<!DOCTYPE html>
<html lang="en">
<head>
<meta charset="utf-8">
<title>BRENTHOLM PTY LTD – Business Card</title>
<link rel="stylesheet" href="https://fonts.googleapis.com/css2?family=Lato:wght@400;700;900&display=swap">
<style>
  :root {
    --bg: #151515;
    --navy: #12206e;
    --navy-text: #142266;
    --gold: #c39133;
    --gold-light: #dcb462;
    --white: #ffffff;
    --ink: #1b2a6b;
  }
  * { box-sizing: border-box; margin: 0; padding: 0; }
  html, body {
    width: 1200px; height: 1122px; overflow: hidden;
    background: var(--bg);
    font-family: "Lato", sans-serif;
  }
  .canvas {
    position: relative; width: 1200px; height: 1122px;
    display: flex; flex-direction: column; align-items: center; justify-content: center; gap: 40px;
  }
  .card {
    position: relative; width: 820px; height: 500px; border-radius: 34px; overflow: hidden;
  }
  /* Front */
  .card--front {
    background: var(--navy);
    display: flex; align-items: center; justify-content: center;
  }
  .brand-front {
    font-weight: 900; font-size: 92px; letter-spacing: 2px; color: var(--gold);
  }
  /* Back */
  .card--back { background: var(--white); color: var(--ink); }
  .brand-back {
    position: absolute; top: 62px; right: 64px;
    font-weight: 900; font-size: 48px; letter-spacing: 1px; color: var(--navy-text);
  }
  .identity { position: absolute; left: 64px; top: 140px; }
  .company { font-weight: 900; font-size: 36px; color: var(--navy-text); letter-spacing: .5px; }
  .person { font-weight: 700; font-size: 24px; color: var(--gold); margin-top: 10px; }
  .role { font-weight: 400; font-size: 24px; color: var(--ink); margin-top: 4px; }
  .rule {
    position: absolute; left: 64px; right: 64px; top: 282px; height: 4px;
    background: linear-gradient(90deg, var(--gold), var(--gold-light) 50%, var(--gold));
  }
  .contacts { position: absolute; left: 64px; top: 310px; list-style: none; }
  .contacts li {
    display: flex; align-items: center; gap: 14px;
    font-size: 24px; line-height: 38px; color: var(--ink);
  }
  .contacts svg { width: 22px; height: 22px; flex: none; }
  .address {
    position: absolute; right: 64px; top: 310px; text-align: right;
    font-size: 22px; line-height: 34px; color: var(--ink);
  }
  .address .strong { font-weight: 700; }
</style>
</head>
<body>
<main class="canvas">
  <section class="card card--front">
    <div class="brand-front">BRENTHOLM</div>
  </section>

  <section class="card card--back">
    <div class="brand-back">BRENTHOLM</div>

    <div class="identity">
      <h1 class="company">BRENTHOLM PTY LTD</h1>
      <p class="person">DORIAN (Dee) KASTELLO</p>
      <p class="role">Director</p>
    </div>

    <div class="rule"></div>

    <ul class="contacts">
      <li>
        <svg viewBox="0 0 24 24" fill="none" stroke="#c39133" stroke-width="2.2" stroke-linecap="round" stroke-linejoin="round"><path d="M5 3h4l2 5-2.5 1.5a11 11 0 0 0 6 6L16 13l5 2v4a2 2 0 0 1-2 2A17 17 0 0 1 3 5a2 2 0 0 1 2-2z"/></svg>
        0412 555 018
      </li>
      <li>
        <svg viewBox="0 0 24 24" fill="none" stroke="#c39133" stroke-width="2.2" stroke-linecap="round"><rect x="6" y="2" width="12" height="20" rx="2"/><line x1="11" y1="18" x2="13" y2="18"/></svg>
        0498 555 207
      </li>
      <li>
        <svg viewBox="0 0 24 24" fill="none" stroke="#c39133" stroke-width="2.2" stroke-linejoin="round"><rect x="2" y="5" width="20" height="14" rx="1"/><path d="M2 6l10 7 10-7"/></svg>
        dk@brentholm-pl.com
      </li>
      <li>
        <svg viewBox="0 0 24 24" fill="none" stroke="#c39133" stroke-width="2.2"><circle cx="12" cy="12" r="10"/><path d="M2 12h20M12 2c3 3 3 17 0 20M12 2c-3 3-3 17 0 20"/></svg>
        brentholm-pl.com
      </li>
    </ul>

    <address class="address" style="font-style:normal">
      PO Box 482<br>
      Elmridge East, Vic 3999<br>
      <span class="strong">ABN- 48 210 775 036</span><br>
      <span class="strong">CDB-U 10458</span>
    </address>
  </section>
</main>
</body>
</html>
```